Looking for a clean, modern, and professional business card design that reflects Valtrim Systems

The design should include the company logo, contact details, and align with our brand identity. Please use a sophisticated and minimalist style, incorporating [specific colors, if applicable]. Creativity is welcome, but the card must maintain a polished and professional appearance.

Details to Include:

Name: Gavin Trelowe
Title: VP Sales / Operations
Company: Valtrim Systems
Phone: 483.216.7705
Email: gavin@valtrimsystems-example.com
Website: www.valtrimsystems-example.com

```html
<!DOCTYPE html>
<html lang="en">
<head>
<meta charset="UTF-8">
<title>Valtrim Systems – Business Card</title>
<link rel="stylesheet" href="https://fonts.googleapis.com/css2?family=Poppins:wght@400;500&display=swap">
<style>
  :root {
    --stage: #e9e7e4;
    --card-blue: #4b73b9;
    --card-blue-light: #5c86c6;
    --card-white: #ffffff;
    --ink-dark: #2a2c30;
    --ink-light: #ffffff;
    --edge-navy: #2c3a63;
  }
  * { box-sizing: border-box; margin: 0; padding: 0; }
  html, body {
    width: 1200px;
    height: 900px;
    overflow: hidden;
  }
  body {
    background: var(--stage);
    font-family: "Poppins", sans-serif;
    position: relative;
  }
  .card {
    position: absolute;
    width: 560px;
    height: 320px;
    border-radius: 4px;
    box-shadow: 0 14px 30px rgba(0,0,0,0.18);
    overflow: hidden;
  }

  /* Back of card (logo side) */
  .card--back {
    left: 580px;
    top: 150px;
    background: var(--card-white);
    border-left: 4px solid var(--edge-navy);
    display: flex;
    align-items: center;
    justify-content: center;
  }
  .card--back .brand-name {
    color: var(--ink-dark);
    font-weight: 500;
    font-size: 34px;
    letter-spacing: 0.04em;
  }

  /* Front of card (contact side) */
  .card--front {
    left: 60px;
    top: 430px;
    background: linear-gradient(135deg, var(--card-blue) 0%, var(--card-blue-light) 100%);
    color: var(--ink-light);
  }
  .card--front .brand-name {
    position: absolute;
    top: 34px;
    right: 36px;
    font-weight: 500;
    font-size: 24px;
    letter-spacing: 0.04em;
    color: var(--ink-light);
  }
  .holder {
    position: absolute;
    left: 44px;
    top: 108px;
  }
  .holder__name {
    font-weight: 500;
    font-size: 36px;
    line-height: 1.1;
    padding-bottom: 6px;
    border-bottom: 1.5px solid var(--ink-light);
    display: inline-block;
  }
  .holder__title {
    font-weight: 400;
    font-size: 18px;
    margin-top: 6px;
  }
  .contact-list {
    position: absolute;
    left: 44px;
    top: 218px;
    list-style: none;
  }
  .contact-list li {
    display: flex;
    align-items: center;
    gap: 18px;
    font-size: 14.5px;
    line-height: 1;
    margin-bottom: 11px;
  }
  .contact-icon {
    width: 18px;
    height: 18px;
    flex: none;
  }
</style>
</head>
<body>

  <section class="card card--back" aria-label="Business card back">
    <span class="brand-name">Valtrim Systems</span>
  </section>

  <section class="card card--front" aria-label="Business card front">
    <span class="brand-name">Valtrim Systems</span>

    <div class="holder">
      <h1 class="holder__name">Gavin Trelowe</h1>
      <p class="holder__title">VP Sales / Operations</p>
    </div>

    <ul class="contact-list">
      <li>
        <svg class="contact-icon" viewBox="0 0 18 18" aria-hidden="true">
          <circle cx="9" cy="9" r="9" fill="#fff"/>
          <path d="M6.2 4.8l1.4 1.9-.8 1c.5 1.1 1.3 1.9 2.3 2.4l1-.8 1.9 1.4-.7 1.5c-3 .2-6.2-3-6-6z" fill="#4b73b9"/>
        </svg>
        483.216.7705
      </li>
      <li>
        <svg class="contact-icon" viewBox="0 0 18 18" aria-hidden="true">
          <circle cx="9" cy="9" r="9" fill="#fff"/>
          <rect x="4.5" y="6" width="9" height="6.5" rx="0.8" fill="none" stroke="#4b73b9" stroke-width="1.2"/>
          <path d="M4.8 6.4L9 9.6l4.2-3.2" fill="none" stroke="#4b73b9" stroke-width="1.2"/>
        </svg>
        gavin@valtrimsystems-example.com
      </li>
      <li>
        <svg class="contact-icon" viewBox="0 0 18 18" aria-hidden="true">
          <circle cx="9" cy="9" r="9" fill="#fff"/>
          <circle cx="9" cy="9" r="4.8" fill="none" stroke="#4b73b9" stroke-width="1.1"/>
          <ellipse cx="9" cy="9" rx="2" ry="4.8" fill="none" stroke="#4b73b9" stroke-width="1.1"/>
          <line x1="4.2" y1="9" x2="13.8" y2="9" stroke="#4b73b9" stroke-width="1.1"/>
        </svg>
        www.valtrimsystems-example.com
      </li>
    </ul>
  </section>

</body>
</html>
```